General Contractors need a new Crisp updated Card Design

We need a new business card design for our company of 25 years based in Toronto call Holvaster Building Inc. : Our goal is to be the leading commercial contractors in Toronto by providing exceptional value to our clients. We work very hard to deliver professional, quality, service in conjunction with consistent price competitiveness to all of our clients on every single project.

Target Market(s)

Design & Build Clients

Industry/Entity Type

Construction Company

Contact Information for Business Card

Address:
18 North Tamlin Glen Road, Unit 57, Marbrook Vale, ON, K7T 2R9
Office: 905-218-5937

Holvasters Logo
Employee Job Description
Employee Cell Phone #
Employee Email
www.holvaster-example.com

Colors

Designer to choose colors to be used in the design.

Requirements
Must have
• Quote Company Saying:
• "Professional. Quality. Service."
Nice to have
• New Crisp up to date look. simple & fresh ( Not to Busy)
Should not have
• NO BLUE PRINTS ON THE BUSINESS CARDS

```html
<!DOCTYPE html>
<html lang="en">
<head>
<meta charset="utf-8">
<title>Holvaster Building Inc. — Business Card</title>
<link rel="stylesheet" href="https://fonts.googleapis.com/css2?family=Cinzel:wght@400;500&family=Fira+Sans+Condensed:wght@300;400;600&display=swap">
<style>
  :root {
    --teal: #00665a;
    --sage: #94ada2;
    --sage-light: #a9c3b8;
    --backdrop: #a6cdca;
  }
  * { box-sizing: border-box; margin: 0; padding: 0; }
  html, body { width: 1200px; height: 1200px; overflow: hidden; }
  body {
    background: var(--backdrop);
    font-family: "Fira Sans Condensed", "Arial Narrow", sans-serif;
    position: relative;
  }
  .card {
    position: absolute;
    left: 280px;
    width: 640px;
    height: 400px;
    overflow: hidden;
  }
  .card--front { top: 170px; background: var(--teal); }
  .card--back { top: 630px; background: var(--sage); }

  /* Front */
  .front__brand {
    position: absolute;
    top: 160px;
    left: 0; right: 0;
    display: flex;
    justify-content: center;
    align-items: center;
    gap: 12px;
  }
  .brand-square {
    width: 30px; height: 30px;
    background: var(--sage-light);
  }
  .brand-name {
    font-family: "Fira Sans Condensed", "Arial Narrow", sans-serif;
    font-weight: 600;
    font-size: 30px;
    letter-spacing: 0.5px;
    color: var(--sage-light);
  }
  .front__tagline {
    position: absolute;
    top: 244px;
    left: 0; right: 0;
    text-align: center;
    font-family: "Cinzel", serif;
    font-size: 17px;
    letter-spacing: 0.6px;
    color: var(--sage);
  }
  .front__address-band {
    position: absolute;
    left: 0; right: 0; bottom: 0;
    height: 74px;
    background: var(--sage);
    display: flex;
    align-items: center;
    justify-content: center;
    gap: 6px;
    font-size: 16px;
    color: var(--teal);
  }
  .icon { width: 15px; height: 15px; flex: none; }

  /* Back */
  .back__shapes { position: absolute; inset: 0; width: 100%; height: 100%; }
  .back__contacts {
    position: absolute;
    top: 42px;
    right: 24px;
    list-style: none;
    text-align: right;
    color: var(--sage-light);
    font-weight: 300;
    font-size: 18px;
  }
  .back__contacts li {
    display: flex;
    justify-content: flex-end;
    align-items: center;
    gap: 7px;
    height: 33.5px;
  }
  .back__contacts .icon { width: 18px; height: 18px; }
  .back__brand {
    position: absolute;
    left: 22px;
    top: 248px;
    display: flex;
    align-items: center;
    gap: 10px;
  }
  .back__brand .brand-square { background: var(--teal); width: 28px; height: 28px; }
  .back__brand .brand-name { color: var(--teal); font-size: 28px; }
  .back__employee {
    position: absolute;
    left: 24px;
    top: 315px;
    font-size: 33px;
    font-weight: 300;
    color: var(--sage-light);
  }
  .back__employee strong { font-weight: 600; }
</style>
</head>
<body>

  <section class="card card--front" aria-label="Card front">
    <div class="front__brand">
      <span class="brand-square"></span>
      <span class="brand-name">Holvaster Building Inc.</span>
    </div>
    <p class="front__tagline">"Professional. Quality. Service."</p>
    <div class="front__address-band">
      <svg class="icon" viewBox="0 0 16 16" aria-hidden="true"><path fill="currentColor" d="M8 0a5.5 5.5 0 0 0-5.5 5.5C2.5 10 8 16 8 16s5.5-6 5.5-10.5A5.5 5.5 0 0 0 8 0zm0 8a2.5 2.5 0 1 1 0-5 2.5 2.5 0 0 1 0 5z"/></svg>
      <span>18 North Tamlin Glen Road, Unit 57, Marbrook Vale, ON, K7T 2R9</span>
    </div>
  </section>

  <section class="card card--back" aria-label="Card back">
    <svg class="back__shapes" viewBox="0 0 557 348" preserveAspectRatio="none" aria-hidden="true">
      <polygon fill="var(--teal)" points="27,22 557,22 557,152 256,152 434,265 0,265 0,327 531,327 434,265 256,152 242,152 409,265 0,265"/>
      <polygon fill="var(--teal)" points="27,22 557,22 557,152 256,152 531,327 0,327 0,265 409,265"/>
      <polygon fill="var(--sage)" points="256,152 557,152 557,327 531,327"/>
    </svg>

    <ul class="back__contacts">
      <li>905-218-5937
        <svg class="icon" viewBox="0 0 16 16" aria-hidden="true"><path fill="currentColor" d="M1 5c0-2 3-3 7-3s7 1 7 3v1.5h-3.5V5h-7v1.5H1zM4 7h8l2 6H2zm4 1.5a2 2 0 1 0 0 4 2 2 0 0 0 0-4z"/></svg>
      </li>
      <li>employees@holvaster-example.com
        <svg class="icon" viewBox="0 0 16 16" aria-hidden="true"><path fill="currentColor" d="M1 3h14v1.5L8 9 1 4.5zm0 3.2L8 10.7l7-4.5V13H1z"/></svg>
      </li>
      <li>www.holvaster-example.com
        <svg class="icon" viewBox="0 0 16 16" aria-hidden="true"><g fill="none" stroke="currentColor" stroke-width="1.3"><circle cx="8" cy="8" r="6.8"/><ellipse cx="8" cy="8" rx="3" ry="6.8"/><path d="M1.2 8h13.6M2.5 4.5h11M2.5 11.5h11"/></g></svg>
      </li>
    </ul>

    <div class="back__brand">
      <span class="brand-square"></span>
      <span class="brand-name">Holvaster Building Inc.</span>
    </div>

    <p class="back__employee">Employees <strong>Name</strong></p>
  </section>

</body>
</html>
```